Media Services Start-up -- Corporate Website and Logo Design. Inspiration required!

We need a logo design and corporate website design, including coding, for our start-up business.
Varnetto’s value proposition is based on bringing together media content from a vast number of geographies globally, adding human and AI curation, translation and editing, and delivering the content using tailored customer interfaces. On the one hand, the business brings together media coverage from all over the world, and on the other it brings together content, human skills and technology to deliver a supreme customer experience.
Varnetto is a B2B media monitoring and analytics business with emphasis on global customers. Varnetto's service offering is centred around sourcing media content from different markets, processing, storing and delivering the content and insights derived from it using an online platform / mobile app.
The messaging we want to create through the logo is:
- Global scope
- Speed of delivery
- Cost-efficiency
- Multi-lingual
- Tailor-made
- Trustworthy
Target Market(s)
Business to business, PR / Communications, Media, Marketing
Logo Text
Varnetto
Coding
Coded - Design and coding required
Number of Pages Required
5+ page
Font styles to use
Other font styles liked:
- See Design Brief for details
Colors
Designer to choose colors to be used in the design.

```html
<!DOCTYPE html>
<html lang="en">
<head>
<meta charset="utf-8">
<title>Varnetto — Solutions</title>
<link href="https://fonts.googleapis.com/css2?family=Questrial&display=swap" rel="stylesheet">
<style>
:root{
  --ink:#0b0b14;
  --text:#2e2e3a;
  --orange:#f26b1d;
  --blue:#4eb0f6;
  --teal:#00bfa5;
  --sand:#f3efeb;
  --navy:#0c1236;
  --accent:#2aa3f0;
  --white:#ffffff;
  --hero-top:#6a74cc;
  --hero-bottom:#2a2c6a;
}
*{box-sizing:border-box;margin:0;padding:0}
html,body{width:1200px;height:2628px;overflow:hidden;background:#fff}
body{font-family:"Questrial",sans-serif;color:var(--text)}
.page{position:relative;width:1200px;height:2628px;overflow:hidden}
.backdrop{position:absolute;left:0;top:0;width:1200px;height:2628px}
.abs{position:absolute}
.topbar-call{left:778px;top:14px;font-size:10px;color:var(--white)}
.btn{background:var(--orange);color:var(--white);font-size:11px;display:flex;align-items:center;justify-content:center;gap:5px}
.btn-learn{left:932px;top:8px;width:99px;height:26px;border-radius:2px}
.btn-learn .dot{width:9px;height:9px;border:1.5px solid #fff;border-radius:50%}
.nav{top:57px;left:584px;display:flex;gap:0;font-size:11.5px;color:var(--white)}
.nav a{color:inherit;text-decoration:none;margin-right:31px}
.hero-title{left:286px;top:160px;font-size:37px;color:var(--white);font-weight:400;letter-spacing:.2px}
.btn-demo{left:287px;top:213px;width:127px;height:30px;font-size:11.5px}
h2.section-title{font-weight:400;font-size:35px;color:var(--ink);letter-spacing:.3px}
.lead{font-size:12.5px;line-height:19px}
.ticks{list-style:none;font-size:12.5px;line-height:19.4px}
.ticks li{position:relative;padding-left:19px}
.ticks li::before{content:"";position:absolute;left:1px;top:5px;width:9px;height:9px;background:var(--accent);
  clip-path:polygon(0 38%,50% 38%,50% 0,100% 50%,50% 100%,50% 62%,0 62%)}
.ticks.on-teal{color:var(--white)}
.ticks.on-teal li::before{background:var(--white)}
.art{position:absolute}
.card{left:87px;top:691px;width:1028px;height:225px;background:var(--white)}
.cta-title{left:0;width:1200px;top:2160px;text-align:center;font-size:45px;color:var(--ink);font-weight:400}
.field{position:absolute;top:2220px;height:37px;border:1px solid #cfcfd4;font-size:11.5px;color:#999;padding:12px 13px}
.btn-start{left:786px;top:2220px;width:166px;height:37px;font-size:11.5px;letter-spacing:.3px}
.footer-col{top:2330px;font-size:12.5px;line-height:23px;color:var(--white)}
.footer-col h4{font-weight:400;font-size:11px;color:var(--accent);margin-bottom:18px;letter-spacing:.2px}
.footer-col .icon{display:inline-block;width:9px;height:9px;margin-right:4px;vertical-align:-1px}
.footer-rule{left:170px;top:2548px;width:860px;height:1px;background:#2a3058}
.copyright{left:0;width:1200px;top:2566px;text-align:center;font-size:10px;color:var(--white)}
</style>
</head>
<body>
<div class="page">
  <svg class="backdrop" viewBox="0 0 1200 2628" aria-hidden="true">
    <defs>
      <linearGradient id="heroGrad" x1="0" y1="0" x2="0" y2="1">
        <stop offset="0" stop-color="var(--hero-top)"/>
        <stop offset="1" stop-color="var(--hero-bottom)"/>
      </linearGradient>
    </defs>
    <polygon points="0,0 1200,0 1200,333 0,260" fill="url(#heroGrad)"/>
    <polygon points="0,675 1200,568 1200,1000 0,1000" fill="var(--blue)"/>
    <polygon points="0,979 1200,855 1200,1353 0,1353" fill="var(--teal)"/>
    <polygon points="0,1746 1200,1650 1200,2150 0,2030" fill="var(--sand)"/>
    <rect x="0" y="2297" width="1200" height="313" fill="var(--navy)"/>
    <rect x="0" y="2610" width="1200" height="18" fill="#ececee"/>
  </svg>

  <div class="abs topbar-call">Call us on: +(61) 02 5550 1873</div>
  <div class="abs btn btn-learn">Learn more <span class="dot"></span></div>
  <nav class="abs nav"><a>Home</a><a>Solutions</a><a>How We Do It</a><a>Our People</a><a>Our Technology</a></nav>
  <h1 class="abs hero-title">Content sourcing, collection and more</h1>
  <div class="abs btn btn-demo">Request a demo</div>

  <section>
    <h2 class="abs section-title" style="left:124px;top:348px">Content Sourcing</h2>
    <p class="abs lead" style="left:124px;top:409px;width:570px">We help you build a content strategy that meets your budget and coverage needs across earned media – Print, Online, TV and Radio.</p>
    <ul class="abs ticks" style="left:124px;top:481px;width:590px">
      <li>Identify geographies and markets of interest</li>
      <li>Build target media source lists to fulfil monitoring and measurement requirements</li>
      <li>Using our transparent cost calculator, we help you with accurate budgeting and choices to ensure you meet your strategy and objectives</li>
      <li>Translate and localise keyword searches and editorial instructions into effecient source-/ country-/ provider-specific needs to minimise wasted content.</li>
    </ul>
    <div class="art" role="img" aria-label="Illustration of a newspaper page with headline and article blocks" style="left:940px;top:345px;width:252px;height:252px;background:linear-gradient(135deg,#fdebdf,#f8c9ad);border-radius:14px"></div>
  </section>

  <section>
    <div class="abs card"></div>
    <div class="art" role="img" aria-label="Icon of devices linked through a cloud" style="left:232px;top:732px;width:143px;height:141px;background:linear-gradient(135deg,#3aa8f0,#a34cf0);border-radius:10px;opacity:.85"></div>
    <h2 class="abs section-title" style="left:546px;top:734px">Content Collection</h2>
    <p class="abs lead" style="left:546px;top:794px;width:440px">We consolidate and manage the delivery of your global media content into a Cloud-based scalable media platform, taking the headache of content management away from your teams.</p>
  </section>

  <section>
    <h2 class="abs section-title" style="left:232px;top:999px">Content Augmentation</h2>
    <ul class="abs ticks on-teal" style="left:155px;top:1051px;width:565px">
      <li>We manage and normalise all of the source-level reference data - country, language, reach etc.</li>
      <li>We add editorial validation to ensure only the content required reaches your delivery, removing inevitable noise from source providers</li>
      <li>Tagging - AI and human based tagging to detect locations, people, topics, products, brands, services, etc.</li>
      <li>Human and automated grouping of stories across geographies - clustering, "also-in" groupings etc.</li>
      <li>Translation summarisation - AI Translation or human-created depending on budget, speed of delivery and need.</li>
      <li>Digest authoring - refining the essence of today's coverage into a concise board-ready output for your organisation</li>
    </ul>
    <div class="art" role="img" aria-label="Illustration of a globe" style="left:904px;top:994px;width:288px;height:288px;border-radius:50%;background:radial-gradient(circle at 40% 40%,#8cc7f5,#4a9ee8)"></div>
  </section>

  <section>
    <div class="art" role="img" aria-label="Illustration of a hand receiving media content" style="left:112px;top:1423px;width:186px;height:192px;border-radius:50%;background:linear-gradient(160deg,#5fc3f5,#3d56a8 60%,#f7a81b)"></div>
    <h2 class="abs section-title" style="left:676px;top:1428px">Content Delivery</h2>
    <ul class="abs ticks" style="left:549px;top:1481px;width:560px">
      <li>Early morning delivery of a consolidated, ready-to-consume media coverage</li>
      <li>Customised email templates, delivering content in templates designed to meet your needs</li>
      <li>Customised platform - modern portal tailored to meet your media management needs, removing the unwanted clutter and focusing on the job at hand</li>
      <li>Integration with Intranets, third-party communication tools e.g. ChatHub, RSS readers, customised APIs</li>
    </ul>
  </section>

  <section>
    <div class="art" role="img" aria-label="Illustration of report pages with charts" style="left:822px;top:1630px;width:363px;height:380px;border-radius:50% 50% 50% 50%/45% 45% 55% 55%;background:linear-gradient(160deg,#dcecfb,#4fc1ef 45%,#3e5ea8)"></div>
    <h2 class="abs section-title" style="left:182px;top:1746px">Media Insights &amp; Consultancy</h2>
    <ul class="abs ticks" style="left:155px;top:1798px;width:565px">
      <li>Levering the normalised content sets from your integrated monitoring service, we can analyse and tag your coverage based on complex qualitative measurement criteria, consistent across all languages and geographies, to combine with quantitative metrics.</li>
      <li>Ability to create a single consistent measurement programme across all of your global operations.</li>
      <li>Consultancy to HQ and local offices on how to utilise and align existing measurement and insight intiatives to provide continuity.</li>
      <li>Customised online dashboards with near real time data insights, coupled with Board-ready offline reporting and export options.</li>
      <li>Integration with social media content, third-party data, point-of-sale, WebStats, and delivering on your Integrated Communications Framework</li>
    </ul>
  </section>

  <section>
    <h2 class="abs cta-title">Learn more about Varnetto</h2>
    <div class="field" style="left:249px;width:165px">Name</div>
    <div class="field" style="left:428px;width:165px">Email</div>
    <div class="field" style="left:607px;width:165px">Phone</div>
    <div class="abs btn btn-start">GET STARTED</div>
  </section>

  <footer>
    <div class="abs footer-col" style="left:170px">
      <h4>VARNETTO</h4>
      <div><svg class="icon" viewBox="0 0 10 10"><path d="M5 0a3.5 3.5 0 0 0-3.5 3.5C1.5 6 5 10 5 10s3.5-4 3.5-6.5A3.5 3.5 0 0 0 5 0zm0 5a1.4 1.4 0 1 1 0-2.8A1.4 1.4 0 0 1 5 5z" fill="#fff"/></svg>48 Harbour Lane, Portsmouth, NH 03801.</div>
      <div><svg class="icon" viewBox="0 0 10 10"><path d="M2 0l2 2.5-1 1.3c.6 1.3 1.6 2.3 2.9 2.9L7.2 5.7 10 7.6 8.6 10C4 10 0 6 0 1.4z" fill="#fff"/></svg>555.014273</div>
      <div><svg class="icon" viewBox="0 0 10 10"><rect x=".5" y="1.5" width="9" height="7" fill="none" stroke="#fff"/><path d="M.5 1.5L5 5.5l4.5-4" fill="none" stroke="#fff"/></svg>info@varnetto.com</div>
    </div>
    <div class="abs footer-col" style="left:467px">
      <h4>SOLUTIONS</h4>
      <div>Content Sourcing</div>
      <div>Content Collection</div>
      <div>Content Augmentation</div>
      <div>Content Delivery</div>
      <div>Media Insights &amp; Consultancy</div>
    </div>
    <div class="abs footer-col" style="left:764px;width:240px">
      <h4>OUR TECHNOLOGY</h4>
      <div style="line-height:19px;margin-bottom:4px">Content Ingestion / Normalisation &amp; Augmentation</div>
      <div>Content Delivery</div>
      <div>Insight Services</div>
    </div>
    <div class="abs footer-rule"></div>
    <div class="abs copyright">© 2019 Varnetto</div>
  </footer>
</div>
</body>
</html>
```